Nine Petals - `Brochure Design Project

We have created a range of Natural & Organic Skincare that we plan on selling to the tourists that visit Australia.

We need a DL sized brochure with approx. 8 x pages designed to reflect a high end Natural & Organic skincare range.

The brand is called 'Quiet Meadow' and the range is called 'Nine Petals'.

The point of difference with our competitors is that each product contains six unique Australian botanicals that have been chosen for their benefits to the skin. I will attach the first draft copy that was written for each product and appears on the packaging.

We also need to make space for a paragraph or two on the background or philosophy behind the ‘Nine Petals’ brand. Why we chose these ingredients, why it is important to use natural & organic ingredients that don’t contain the harmful parabens etc.. The design should have images that refer to that fact that the product is uniquely Australian, natural & organic and should draw on the benefits that Australia is perceived as a ‘pure’, ‘clean’ and ‘natural’ environment.

I have also attached the product artwork for your reference – please note that the gold colour is gold foil. We have samples of the printed boxes and they look great. We do not have product photo's yet and will need positionals from you before we do.

We have the following products in the range. All (except the Lip Balm) contain the six Australian botanicals.

1. Lanolin Lip Balm
2. Lanolin Body Cream
3. Lanolin day cream
4. Placenta (plant) Cream
5. Placenta (plant) Serum
6. Collagen Cream
7. Collagen Serum

The featured products are the Placenta and Collagen products. The lanolin products are secondary.

We do not have images of the Lanolin Body cream or Lip balm. Please simply create positionals.

Please let me know if there is anything else you require.

Reason: I am currently away and will be returning to the office on 10th October. Thank you.

Target Market(s)

Customers are paying a premium so the design must reflect this.

Customers that like Natural & Organic products.

We have included gold foil in the packaging to reflect a high end product. We have also included gold foil as a large part of our target marget is Asian, in particula Chinese. In saying this, the design needs to appeal to both Western and Asian customers.

Industry/Entity Type

Environment

Requirements
Nice to have
• Nature images
Beautiful lady images
Lifestyle images

The design should include the above features but at the same time reflect a classy, high end range.

```html
<!DOCTYPE html>
<html lang="en">
<head>
<meta charset="utf-8">
<title>Quiet Meadow Nine Petals – Botanicals Spread</title>
<link rel="stylesheet" href="https://fonts.googleapis.com/css2?family=Arimo:wght@400&family=Caveat:wght@500&display=swap">
<style>
  :root {
    --backdrop: #ece9e2;
    --paper: #fbf8ee;
    --fold: #d9d4c4;
    --gold: #c9a012;
    --gold-edge: #a8830a;
    --script-green: #2f5a1e;
    --olive: #7d8c2c;
    --olive-deep: #66741f;
    --body-ink: #2b2b2b;
    --on-gold: #ffffff;
  }
  * { margin: 0; padding: 0; box-sizing: border-box; }
  html, body { width: 1200px; height: 900px; overflow: hidden; background: var(--backdrop); }
  .spread {
    position: absolute; left: 40px; top: 152px; width: 1120px; height: 596px;
    background: var(--paper);
    box-shadow: 0 2px 8px rgba(0,0,0,0.18);
    font-family: "Arimo", Arial, sans-serif;
  }
  .fold { position: absolute; top: 0; bottom: 0; width: 1px; background: var(--fold); }
  .fold--left { left: 297px; }
  .fold--right { left: 709px; }

  .hero-photo {
    position: absolute; left: 0; top: 0; width: 297px; height: 323px;
    background: radial-gradient(ellipse at 45% 55%, #b8391f 0%, #9c4a22 25%, #a07a2c 55%, #c9ad52 80%, #b89a3e 100%);
  }
  .intro { position: absolute; left: 38px; top: 358px; width: 224px; color: var(--body-ink); }
  .intro__title { font-family: "Caveat", cursive; font-weight: 500; font-size: 15px; color: var(--script-green); margin-bottom: 6px; }
  .intro p { font-size: 8.4px; line-height: 10.6px; text-align: justify; margin-bottom: 10px; }

  .map {
    position: absolute; left: 330px; top: 0; width: 790px; height: 596px;
    background:
      radial-gradient(ellipse 48% 44% at 30% 52%, var(--olive) 0%, var(--olive) 60%, rgba(125,140,44,0) 100%),
      radial-gradient(ellipse 40% 48% at 66% 44%, var(--olive-deep) 0%, var(--olive) 55%, rgba(125,140,44,0) 100%);
  }

  .botanical { position: absolute; display: flex; height: 70px; }
  .botanical__photo { width: 90px; height: 100%; }
  .botanical__card {
    width: 208px; height: 100%; background: var(--gold);
    border-left: 4px solid var(--gold-edge);
    padding: 5px 9px 0 8px; color: var(--on-gold);
  }
  .botanical__name { font-family: "Caveat", cursive; font-weight: 500; font-size: 14px; line-height: 14px; color: var(--script-green); margin-bottom: 2px; }
  .botanical__text { font-size: 8px; line-height: 10px; text-align: justify; }

  .botanical--davidson { left: 335px; top: 84px; }
  .botanical--davidson .botanical__photo { background: linear-gradient(135deg, #5a2a4a, #8b4e74 50%, #3d1c33); }
  .botanical--avocado { left: 411px; top: 256px; height: 72px; }
  .botanical--avocado .botanical__photo { background: radial-gradient(circle at 50% 55%, #a8622d 0%, #a8622d 22%, #d8d486 30%, #6d7d2c 70%, #8a8a70 100%); }
  .botanical--vitamin { left: 338px; top: 445px; height: 90px; }
  .botanical--vitamin .botanical__photo { width: 88px; background: linear-gradient(160deg, #c8b070, #8f8a4a 50%, #5e6a3a); }
  .botanical--kakadu { left: 712px; top: 26px; }
  .botanical--kakadu .botanical__photo { width: 88px; background: radial-gradient(circle at 40% 40%, #b9d46b, #7fa035 60%, #4f6b22); }
  .botanical--rosella { left: 781px; top: 175px; }
  .botanical--rosella .botanical__photo { background: radial-gradient(circle at 50% 50%, #a3162a 0%, #7a1020 40%, #5d7a3a 80%); }
  .botanical--rosehip { left: 755px; top: 378px; }
  .botanical--rosehip .botanical__photo { background: radial-gradient(circle at 40% 50%, #c42a2a 0%, #b33a3a 35%, #d6d0c4 75%, #eeeae2 100%); }

  .brand-mark { position: absolute; left: 1010px; top: 490px; width: 100px; display: flex; flex-direction: column; align-items: center; gap: 8px; }
  .brand-mark__dot { width: 30px; height: 30px; border-radius: 50%; background: var(--olive-deep); }
  .brand-mark__name { font-size: 15px; color: var(--olive-deep); white-space: nowrap; }
</style>
</head>
<body>
  <main class="spread">
    <div class="hero-photo" role="img" aria-label="Photograph of red rosehips on a branch with autumn leaves"></div>
    <section class="intro">
      <h2 class="intro__title">Quiet Meadow™ Nine Petals Skincare</h2>
      <p>Inspired by Australian's exceptional botanical variety, Quiet Meadow™ has developed a new range of all natural skin care products. A luxurious blend of natural and active organic ingredients have been added to leave your skin more balance, youthful and vibrant.</p>
      <p>The secret of timeless beauty is radiant and healthy looking skin. Despite constant exposure to the harsh effects of wind, sun and pollution, your skin naturally has an amazing ability to protect, renew and regenerate its cells. With time however, this ability diminishes and your skin becomes more vulnerable, showing signs of aging. Quiet Meadow™ Nine Petals skin care products treat much more than just appearances – They support and nourish your skin from within and stimulate its natural process to replenish cells and to rejuvenate.</p>
    </section>

    <div class="fold fold--left"></div>
    <div class="map" role="img" aria-label="Textured olive green map of Australia spanning both pages"></div>
    <div class="fold fold--right"></div>

    <article class="botanical botanical--davidson">
      <div class="botanical__photo" role="img" aria-label="Photograph of purple Davidson plums"></div>
      <div class="botanical__card">
        <h3 class="botanical__name">Davidson Plum</h3>
        <p class="botanical__text">A native Australian fruit found in the rainforests of Queensland. It contains high levels of anti-oxidants. This provides significant hydration for the skin and strengthens elasticity.</p>
      </div>
    </article>

    <article class="botanical botanical--avocado">
      <div class="botanical__photo" role="img" aria-label="Photograph of a halved avocado"></div>
      <div class="botanical__card">
        <h3 class="botanical__name">Organic Avocado</h3>
        <p class="botanical__text">Provides a rich source of Vitamin A, B, D and E. It penetrates the skin evenly and quickly, allowing skin to be smooth and moisturised.</p>
      </div>
    </article>

    <article class="botanical botanical--vitamin">
      <div class="botanical__photo" role="img" aria-label="Photograph of wheat ears"></div>
      <div class="botanical__card">
        <h3 class="botanical__name">Vitamin E</h3>
        <p class="botanical__text">A strong anti-oxidant vital in protecting skin cells from UV light, pollution and other elements that can damage the skin. It helps improves overall skin health by deeply penetrating the skin to reduce the appearance of deep wrinkles, dry and cracked skin.</p>
      </div>
    </article>

    <article class="botanical botanical--kakadu">
      <div class="botanical__photo" role="img" aria-label="Photograph of green Kakadu plums"></div>
      <div class="botanical__card">
        <h3 class="botanical__name">Kakadu Plum</h3>
        <p class="botanical__text">One of the world's richest sources of Vitamin C. The plant is found in Northern Australia. It is used most commonly in skincare to brighten and plump the skin, giving it a youthful appearance.</p>
      </div>
    </article>

    <article class="botanical botanical--rosella">
      <div class="botanical__photo" role="img" aria-label="Photograph of a red rosella hibiscus calyx"></div>
      <div class="botanical__card">
        <h3 class="botanical__name">Rosella Extract</h3>
        <p class="botanical__text">A native species of hibiscus and high in anti-oxidants. It stimulates a natural, healthy metabolism for optimal skin cell renewal.</p>
      </div>
    </article>

    <article class="botanical botanical--rosehip">
      <div class="botanical__photo" role="img" aria-label="Photograph of frosted red rosehips"></div>
      <div class="botanical__card">
        <h3 class="botanical__name">Organic Rosehip Oil</h3>
        <p class="botanical__text">Rich in Vitamin E &amp; Omega 3, 6 and 9 essential fatty acids. Your skin will be comforted, deeply moisturised, look vibrant, feeling smooth and soft.</p>
      </div>
    </article>

    <div class="brand-mark">
      <span class="brand-mark__dot"></span>
      <span class="brand-mark__name">Nine Petals</span>
    </div>
  </main>
</body>
</html>
```